Online Marketing Agency Website

We are an online marketing agency that specializes in search marketing (SEM) for businesses of all sizes. Our core services include local search marketing, seo, paid search, paid social, graphic design, video production/editing and website design. We have an existing website that we launched a number of years ago but it's very outdated and we're currently too busy to design a new version.

Target Market(s)

Any business that needs online marketing services with an emphasis on search marketing.

Industry/Entity Type

Ad Agency

Number of Pages Required

4 page

Font styles to use
Sans Serif

Requirements
Must have
• Home page, interior page, blog page, contact us page.
Look and feel should be modern and clean and easy to navigate.
Sections for call outs for specific services: Business Marketing Strategy, Content Creation and Marketing, Graphic & Publication Design, Pay Per Click (PPC) Management, Search Engine Optimization, Social Media Management, Video Production & Editing, Website Hosting & Management, Website Design & Development
Use color from logo that was uploaded.

```html
<!DOCTYPE html>
<html lang="en">
<head>
<meta charset="utf-8">
<title>Apex Signal — Search-Led Growth Studio</title>
<link rel="stylesheet" href="https://fonts.googleapis.com/css2?family=Montserrat:wght@400;500;600;700;800&display=swap">
<style>
:root{
  --orange:#f04a14;
  --orange-soft:#ff6a2b;
  --ink:#2b2d3a;
  --text:#4a4d5a;
  --muted:#6d7080;
  --mint:#e3f6f3;
  --mint-strong:#cdeee9;
  --blue:#2a8fd6;
  --green:#5cc85a;
  --white:#ffffff;
  --card-shadow:0 6px 22px rgba(40,60,80,.10);
}
*{box-sizing:border-box;margin:0;padding:0}
html,body{width:1200px;height:4372px;overflow:hidden}
body{position:relative;background:var(--white);font-family:'Montserrat',sans-serif;color:var(--text)}
.abs{position:absolute}
a{color:inherit;text-decoration:none}

.blob{position:absolute;background:var(--mint);border-radius:50%}

/* header */
.brand{position:absolute;left:82px;top:44px;width:130px;text-align:center}
.brand-mark{width:26px;height:26px;border-radius:50%;background:var(--orange);margin:0 auto 6px}
.brand-name{font-weight:700;font-size:14px;color:var(--ink);letter-spacing:.3px}
.brand-tag{font-weight:700;font-size:8.5px;color:var(--ink);letter-spacing:.2px;margin-top:1px}
.nav{position:absolute;top:45px;left:0;font-size:13px;color:var(--text)}
.nav a{position:absolute;white-space:nowrap}
.nav a.active{color:var(--orange)}
.call{position:absolute;left:916px;top:45px;font-size:13px;white-space:nowrap;color:var(--text)}
.call b{color:var(--ink);font-weight:700}
.search{position:absolute;left:1116px;top:42px}

.social{position:absolute;left:1164px;width:36px}
.social span{display:block;width:36px;height:34px;margin-bottom:1px}
.s1{background:#3b5a9a}.s2{background:#2aa3e0}.s3{background:#e0432f}.s4{background:#f07c22}

/* hero */
.hero-kicker{position:absolute;left:90px;top:222px;font-size:20px;font-weight:500;color:var(--ink);letter-spacing:.5px}
.hero-title{position:absolute;left:88px;top:254px;font-size:50px;line-height:56px;font-weight:800;color:var(--ink)}
.hero-copy{position:absolute;left:92px;top:388px;font-size:14.5px;line-height:25px;color:var(--text)}
.btn-solid{position:absolute;display:flex;align-items:center;justify-content:center;background:var(--orange);color:var(--white);font-size:12.5px;font-weight:700;letter-spacing:.3px}
.hero-art{position:absolute;left:543px;top:68px;width:657px;height:611px}

/* services */
.section-title{position:absolute;left:0;width:1200px;text-align:center;font-size:30px;font-weight:800;color:var(--ink);letter-spacing:.3px}
.services-intro{position:absolute;left:0;top:848px;width:1200px;text-align:center;font-size:13.5px;line-height:25.5px;color:var(--text)}
.person-ph{position:absolute;left:30px;top:976px;width:310px;height:908px;border-radius:140px 140px 60px 60px;background:linear-gradient(180deg,#f3ece6,#e8ddd4)}
.card{position:absolute;width:238px;height:270px;background:var(--white);border-radius:6px;box-shadow:var(--card-shadow)}
.card.featured{border:3px solid var(--orange)}
.card-icon{position:absolute;left:26px;top:18px;width:86px;height:86px;border-radius:50%;background:var(--mint);display:flex;align-items:center;justify-content:center}
.card.featured .card-icon{background:var(--orange)}
.card-title{position:absolute;left:30px;top:114px;font-size:16.5px;line-height:26px;font-weight:600;color:var(--ink)}
.card-rule{position:absolute;left:30px;top:174px;width:30px;height:2px;background:var(--orange)}
.card-copy{position:absolute;left:30px;top:194px;font-size:13px;line-height:25px;color:var(--text)}

/* feature */
.feature-art{position:absolute;left:0;top:2020px;width:530px;height:590px}
.eyebrow{position:absolute;font-size:16.5px;font-weight:600;color:var(--ink)}
.feature-title{position:absolute;left:609px;top:2236px;font-size:30px;font-weight:800;color:var(--ink);letter-spacing:.2px}
.feature-copy{position:absolute;left:610px;top:2302px;font-size:13.5px;line-height:25.5px;color:var(--text)}
.btn-outline{position:absolute;left:614px;top:2420px;width:133px;height:41px;border:1.5px solid var(--ink);display:flex;align-items:center;justify-content:center;font-size:12.5px;font-weight:700;color:var(--ink)}

/* work */
.work{position:absolute;top:2855px;width:329px;height:231px}
.work-1{left:80px;background:linear-gradient(180deg,#eef1f4,#cfd6de);border-top:5px solid #1f4d6b}
.work-2{left:431px;background:linear-gradient(160deg,#ff6a2b,#e8400f);color:var(--white);text-align:center}
.work-2 h3{margin-top:52px;font-size:17.5px;font-weight:700}
.work-2 .rule{width:34px;height:2px;background:var(--white);margin:9px auto 12px}
.work-2 p{font-size:13px;line-height:26px}
.work-3{left:781px;background:linear-gradient(135deg,#2b3138,#4a525c 55%,#dfe3e6 56%,#c9ced3)}
.arrows{position:absolute;top:3140px;left:572px;display:flex;gap:14px}

/* contact band */
.contact-band{position:absolute;left:0;top:3344px;width:1200px;height:529px;background:linear-gradient(110deg,#3a9b4a,#6fd468 45%,#4fbf57 75%,#3a9a50)}
.contact-circle{position:absolute;left:64px;top:3334px;width:526px;height:500px;border-radius:50%;background:var(--blue)}
.contact-head{position:absolute;left:64px;width:526px;text-align:center;color:var(--white)}
.field{position:absolute;width:166px;border-bottom:1px solid rgba(255,255,255,.85);font-size:13.5px;color:var(--white);padding-bottom:6px}
.btn-white{position:absolute;left:272px;top:3734px;width:132px;height:42px;background:var(--white);color:var(--ink);font-size:12.5px;font-weight:700;display:flex;align-items:center;justify-content:center}
.privacy{position:absolute;right:100px;top:3803px;text-align:right;font-size:13.5px;line-height:25px;color:var(--white)}

/* footer */
.footer-brand{position:absolute;left:112px;top:3950px;width:134px;text-align:center}
.footer-about{position:absolute;left:115px;top:4058px;font-size:13.5px;line-height:25.5px;color:var(--text)}
.footer-col{position:absolute;top:3956px}
.footer-col h4{font-size:16.5px;font-weight:600;color:var(--ink);margin-bottom:16px}
.footer-col li{list-style:none;font-size:13px;line-height:25.8px;color:var(--text)}
.contact-line{display:flex;align-items:center;gap:14px;font-size:13px;line-height:27px;color:var(--text)}
.copyright{position:absolute;left:0;width:1200px;top:4270px;text-align:center;font-size:12.5px;color:var(--text)}
</style>
</head>
<body>

<div class="blob" style="left:-160px;top:720px;width:700px;height:700px;opacity:.55"></div>
<div class="blob" style="left:1060px;top:1280px;width:300px;height:360px;opacity:.8"></div>
<div class="blob" style="left:320px;top:2690px;width:560px;height:560px;opacity:.55"></div>
<div class="blob" style="left:-150px;top:3960px;width:400px;height:340px;opacity:.6"></div>
<div class="blob" style="left:306px;top:140px;width:126px;height:84px;border-radius:50%;background:#eef3f6"></div>

<!-- header -->
<div class="brand">
  <div class="brand-mark"></div>
  <div class="brand-name">APEX SIGNAL</div>
  <div class="brand-tag">SEARCH-LED GROWTH</div>
</div>
<nav class="nav">
  <a class="active" style="left:294px">Home</a>
  <a style="left:365px">Our Services</a>
  <a style="left:480px">Featured Work</a>
  <a style="left:607px">Blog</a>
  <a style="left:667px">About</a>
  <a style="left:738px">Contact</a>
</nav>
<div class="call">Call us at <b>800-555-0142</b></div>
<svg class="search" width="20" height="20" viewBox="0 0 20 20"><circle cx="8" cy="8" r="6" fill="none" stroke="#4a4d5a" stroke-width="1.6"/><line x1="12.5" y1="12.5" x2="18" y2="18" stroke="#4a4d5a" stroke-width="1.8"/></svg>

<div class="social" style="top:209px"><span class="s1"></span><span class="s2"></span><span class="s3"></span><span class="s4"></span></div>

<!-- hero -->
<div class="hero-kicker">WELCOME</div>
<h1 class="hero-title">Local SEO &amp;<br>Business Listings</h1>
<p class="hero-copy">85% of Consumers Use the Internet to Find Local<br>Businesses. Are They Finding Yours?</p>
<a class="btn-solid" style="left:92px;top:463px;width:132px;height:41px">CONTACT US</a>

<svg class="hero-art" viewBox="0 0 657 611" role="img" aria-label="Photo of a team collaborating around laptops with map-pin network graphics">
  <defs><linearGradient id="heroFill" x1="0" y1="0" x2="1" y2="1"><stop offset="0" stop-color="#c9dbea"/><stop offset=".6" stop-color="#7fa3c6"/><stop offset="1" stop-color="#3f6b9c"/></linearGradient></defs>
  <path d="M120 30 C170 0 250 60 330 20 C420 -20 520 10 657 0 L657 470 C600 560 470 600 330 590 C200 580 90 560 30 470 C-20 390 20 300 60 220 C100 140 70 60 120 30 Z" fill="url(#heroFill)"/>
  <path d="M30 470 C90 560 200 590 330 595 C470 600 600 560 657 470" fill="none" stroke="#f04a14" stroke-width="12"/>
  <path d="M120 30 C80 60 100 130 60 210" fill="none" stroke="#f04a14" stroke-width="8"/>
</svg>

<!-- services -->
<h2 class="section-title" style="top:782px">OUR SERVICES</h2>
<p class="services-intro">Apex Signal is a full-service online marketing agency.<br>We can handle any element of your online marketing so you can get back to doing what you do<br>best — growing your business. All of our services are offered on an ‘a la carte’ basis.<br>The following are just a few of the core services we offer:</p>

<div class="person-ph" role="img" aria-label="Photo of a smiling woman in a white dress presenting the services"></div>

<div class="card featured" style="left:356px;top:996px">
  <div class="card-icon"><svg width="44" height="44" viewBox="0 0 44 44" fill="none" stroke="#fff" stroke-width="2.4"><circle cx="22" cy="22" r="18"/><circle cx="14" cy="16" r="3"/><path d="M26 12l6 6M32 12l-6 6M13 28l6 6M19 28l-6 6M18 18l10 12"/></svg></div>
  <div class="card-title">Business Marketing<br>Strategy</div><div class="card-rule"></div>
  <div class="card-copy">You’ve heard it before.<br>“Content is king.”</div>
</div>
<div class="card" style="left:621px;top:996px">
  <div class="card-icon"><svg width="44" height="44" viewBox="0 0 44 44" fill="none" stroke="#f04a14" stroke-width="2.4"><rect x="6" y="10" width="28" height="26" rx="2"/><path d="M11 18h18M11 24h12M11 30h14M30 22l8-10"/></svg></div>
  <div class="card-title">Content Creation<br>and Marketing</div><div class="card-rule"></div>
  <div class="card-copy">You’ve heard it before.<br>“Content is king.”</div>
</div>
<div class="card" style="left:886px;top:996px">
  <div class="card-icon"><svg width="44" height="44" viewBox="0 0 44 44" fill="none" stroke="#f04a14" stroke-width="2.4"><path d="M22 12c-5-4-11-4-16-3v25c5-1 11-1 16 3 5-4 11-4 16-3V9c-5-1-11-1-16 3zM22 12v25"/></svg></div>
  <div class="card-title">Graphic &amp;<br>Publication Design</div><div class="card-rule"></div>
  <div class="card-copy">You’ve heard it before.<br>“Content is king.”</div>
</div>

<div class="card" style="left:356px;top:1293px">
  <div class="card-icon"><svg width="44" height="44" viewBox="0 0 44 44" fill="none" stroke="#f04a14" stroke-width="2.6"><circle cx="22" cy="22" r="16"/><circle cx="22" cy="22" r="9"/><circle cx="22" cy="22" r="3"/><path d="M22 22l14-14"/></svg></div>
  <div class="card-title">Pay Per Click (PPC)<br>Management</div><div class="card-rule"></div>
  <div class="card-copy">You’ve heard it before.<br>“Content is king.”</div>
</div>
<div class="card" style="left:621px;top:1293px">
  <div class="card-icon"><svg width="44" height="44" viewBox="0 0 44 44" fill="none" stroke="#f04a14" stroke-width="2.4"><rect x="5" y="9" width="30" height="24" rx="2"/><path d="M10 16h14M10 22h10"/><circle cx="30" cy="28" r="6"/><path d="M34 32l6 6"/></svg></div>
  <div class="card-title">Search Engine<br>Optimization</div><div class="card-rule"></div>
  <div class="card-copy">You’ve heard it before.<br>“Content is king.”</div>
</div>
<div class="card" style="left:886px;top:1293px">
  <div class="card-icon"><svg width="44" height="44" viewBox="0 0 44 44" fill="none" stroke="#f04a14" stroke-width="2.4"><path d="M6 20c0-7 6-12 14-12s14 5 14 12-6 12-14 12c-2 0-4 0-6-1l-7 4 2-6c-2-2-3-6-3-9z"/><circle cx="14" cy="20" r="1.5" fill="#f04a14"/><circle cx="20" cy="20" r="1.5" fill="#f04a14"/><circle cx="26" cy="20" r="1.5" fill="#f04a14"/></svg></div>
  <div class="card-title">Social Media<br>Management</div><div class="card-rule"></div>
  <div class="card-copy">You’ve heard it before.<br>“Content is king.”</div>
</div>

<div class="card" style="left:356px;top:1592px">
  <div class="card-icon"><svg width="44" height="44" viewBox="0 0 44 44" fill="none" stroke="#f04a14" stroke-width="2.4"><rect x="6" y="8" width="32" height="28" rx="2"/><path d="M12 8v28M32 8v28M19 16l9 6-9 6z"/></svg></div>
  <div class="card-title">Video Production<br>&amp; Editing</div><div class="card-rule"></div>
  <div class="card-copy">You’ve heard it before.<br>“Content is king.”</div>
</div>
<div class="card" style="left:621px;top:1592px">
  <div class="card-icon"><svg width="44" height="44" viewBox="0 0 44 44" fill="none" stroke="#f04a14" stroke-width="2.4"><rect x="6" y="8" width="32" height="28" rx="2"/><path d="M6 15h32"/><circle cx="22" cy="26" r="6"/><path d="M22 17v3M22 32v3M13 26h3M28 26h3"/></svg></div>
  <div class="card-title">Website Hosting &amp;<br>Management</div><div class="card-rule"></div>
  <div class="card-copy">You’ve heard it before.<br>“Content is king.”</div>
</div>
<div class="card" style="left:886px;top:1592px">
  <div class="card-icon"><svg width="44" height="44" viewBox="0 0 44 44" fill="none" stroke="#f04a14" stroke-width="2.4"><rect x="4" y="8" width="30" height="22" rx="2"/><path d="M14 36h10M19 30v6"/><rect x="30" y="18" width="10" height="18" rx="2"/></svg></div>
  <div class="card-title">Website Design &amp;<br>Development</div><div class="card-rule"></div>
  <div class="card-copy">You’ve heard it before.<br>“Content is king.”</div>
</div>

<!-- feature -->
<svg class="feature-art" viewBox="0 0 530 590" role="img" aria-label="Photo of a smiling man in a striped shirt holding a phone beside a laptop">
  <defs><linearGradient id="featFill" x1="0" y1="0" x2="1" y2="1"><stop offset="0" stop-color="#7fc0dc"/><stop offset="1" stop-color="#2b7fae"/></linearGradient></defs>
  <path d="M0 80 C80 70 160 10 260 2 C360 -6 420 40 440 110 C460 190 410 250 440 330 C470 410 540 470 500 540 C460 600 360 590 280 560 C190 530 90 520 0 500 Z" fill="url(#featFill)"/>
  <path d="M0 510 C90 530 190 540 280 570 C360 596 470 600 515 530" fill="none" stroke="#f04a14" stroke-width="14"/>
</svg>
<svg class="abs" style="left:946px;top:2142px" width="62" height="62" viewBox="0 0 44 44" fill="none" stroke="#d5d8dd" stroke-width="2"><circle cx="22" cy="22" r="18"/><circle cx="14" cy="16" r="3"/><path d="M26 12l6 6M32 12l-6 6M13 28l6 6M19 28l-6 6M18 18l10 12"/></svg>
<div class="eyebrow" style="left:610px;top:2199px">Content</div>
<h2 class="feature-title">BUSINESS MARKETING STRATEGY</h2>
<p class="feature-copy">Let us strategize the big picture for you. With decades of experience,<br>we have seen what works and what doesn’t. And we can leverage all<br>that experience for your business.</p>
<a class="btn-outline">CONTACT US</a>

<!-- featured work -->
<div class="eyebrow" style="left:0;width:1182px;text-align:center;top:2718px">Content</div>
<h2 class="section-title" style="top:2752px;width:1194px">FEATURED WORK</h2>
<div class="work work-1" role="img" aria-label="Screenshot of a law firm website project"></div>
<div class="work work-2" role="img" aria-label="Digital signage project for a seafood festival">
  <h3>Digital Signage Content</h3><div class="rule"></div>
  <p>Apex Signal is a full-service online<br>marketing agency.</p>
  <p style="margin-top:10px">Posted on January 16, 2016</p>
</div>
<div class="work work-3" role="img" aria-label="Stationery and business card branding project"></div>
<div class="arrows">
  <svg width="12" height="16" viewBox="0 0 12 16"><path d="M9 2L3 8l6 6" fill="none" stroke="#4a4d5a" stroke-width="1.6"/></svg>
  <svg width="12" height="16" viewBox="0 0 12 16"><path d="M3 2l6 6-6 6" fill="none" stroke="#4a4d5a" stroke-width="1.6"/></svg>
</div>

<!-- contact band -->
<div class="contact-band" role="img" aria-label="Green-toned photo of a team working together at a table"></div>
<div class="contact-circle"></div>
<div class="contact-head" style="top:3412px;font-size:16.5px;font-weight:600">Content</div>
<div class="contact-head" style="top:3446px;font-size:28px;font-weight:800">NEED A LIFT?</div>
<div class="contact-head" style="top:3497px;font-size:13.5px;line-height:26px">Interested in working with us?<br>Fill out the form below or give us a call!</div>
<div class="field" style="left:156px;top:3594px">Name</div>
<div class="field" style="left:353px;top:3594px">Email</div>
<div class="field" style="left:156px;top:3653px">Phone</div>
<div class="field" style="left:353px;top:3653px">How can we help you?</div>
<a class="btn-white">GET STARTED</a>
<p class="privacy">We take your privacy seriously.<br>We will not spam you or give out your information to anyone.</p>

<!-- footer -->
<div class="footer-brand">
  <div class="brand-mark"></div>
  <div class="brand-name">APEX SIGNAL</div>
  <div class="brand-tag">SEARCH-LED GROWTH</div>
</div>
<p class="footer-about">We focus on the needs of small<br>to middle market businesses to<br>improve and grow their return.</p>
<div class="footer-col" style="left:459px">
  <h4>Company</h4>
  <ul><li>Home</li><li>Our Services</li><li>Featured Work</li><li>Blog</li><li>About</li><li>Contact</li></ul>
</div>
<div class="footer-col" style="left:674px">
  <h4>Projects</h4>
  <ul><li>Home</li><li>Our Services</li><li>Featured Work</li><li>Blog</li><li>About</li><li>Contact</li></ul>
</div>
<div class="footer-col" style="left:862px">
  <h4>Contacts</h4>
  <div class="contact-line"><svg width="18" height="18" viewBox="0 0 18 18"><path d="M4 2l3 3-2 2c1 2 3 4 5 5l2-2 3 3-2 3C8 16 2 10 2 4z" fill="none" stroke="#f04a14" stroke-width="1.4"/></svg>800-555-0142</div>
  <div class="contact-line"><svg width="18" height="18" viewBox="0 0 18 18"><rect x="2" y="4" width="14" height="10" fill="none" stroke="#f04a14" stroke-width="1.4"/><path d="M2 4l7 6 7-6" fill="none" stroke="#f04a14" stroke-width="1.4"/></svg>hello@apexsignal.com</div>
</div>
<div class="social" style="top:3997px"><span class="s1"></span><span class="s2"></span><span class="s3"></span><span class="s4"></span></div>
<div class="copyright">COPYRIGHT © 2020 APEX SIGNAL LLC. ALL RIGHTS RESERVED.</div>

</body>
</html>
```